Cleaning Company Website Design

I am looking for a website design that has my contact information on each page (Call or Text and my e-mail). It should have the main landing page and than pages for Residential Cleaning (Move In/Move Out, Weekly, and Bi-Weekly Cleaning), Commercial Cleaning (Move In/Move Out, Weekly, and Bi-Weekly Cleaning), New Construction Cleaning (Residential, Commercial, and Industrial), and Apartment Turn cleaning for Property Managers. It should list that we carry insurance as well.

Target Market(s)

Residential and Commercial Customers

Industry/Entity Type

Cleaning

Coding

Coded - Design and coding required

Number of Pages Required

5+ page

Requirements
Must have
• A clean professional looking website

```html
<!DOCTYPE html>
<html lang="en">
<head>
<meta charset="utf-8">
<title>ClearSpot Cleaning</title>
<link href="https://fonts.googleapis.com/css2?family=Montserrat:wght@400;500;600;700;800&family=Roboto+Slab:wght@500;600&family=Roboto:wght@400;500;700&family=Roboto+Condensed:wght@600&display=swap" rel="stylesheet">
<style>
:root{
  --blue:#2f80c6;
  --blue-dark:#1f6aad;
  --teal:#2db4a6;
  --ink:#1d1d1d;
  --muted:#444;
  --soft:#f3f3f3;
  --footer:#0c0c0c;
  --white:#fff;
}
*{box-sizing:border-box;margin:0;padding:0}
html,body{width:1200px;height:4158px;overflow:hidden}
body{font-family:'Roboto',sans-serif;color:var(--ink);background:var(--white);position:relative}
.wrap{width:918px;margin:0 auto;position:relative}
.btn{display:inline-block;background:var(--blue);color:var(--white);font:500 13px 'Roboto',sans-serif;border-radius:18px;padding:9px 21px;text-decoration:none}
.section-title{font:600 34px 'Roboto Slab',serif;color:var(--blue);text-align:center}

/* header */
.site-header{height:120px;position:relative}
.topbar{position:absolute;left:336px;right:0;top:0;height:42px;background:var(--blue);clip-path:polygon(22px 0,100% 0,100% 100%,0 100%);display:flex;align-items:center;padding-left:34px;color:var(--white);font:500 14px 'Montserrat',sans-serif;gap:24px}
.topbar b{font-size:18px;font-weight:700}
.topbar .item{display:flex;align-items:center;gap:8px}
.socials{display:flex;gap:6px;margin-left:6px}
.socials span{width:26px;height:26px;border-radius:50%;background:var(--white);display:block}
.logo{position:absolute;left:141px;top:26px;display:flex;align-items:center;gap:10px;font:700 22px 'Montserrat',sans-serif;color:var(--teal)}
.logo i{width:34px;height:34px;background:var(--blue);display:block;border-radius:4px}
.nav{position:absolute;left:373px;top:62px;display:flex;align-items:center;gap:32px;font:500 14px 'Montserrat',sans-serif;color:#333}
.nav .active{color:var(--blue)}
.nav .quote{position:absolute;left:523px;top:0px;margin-top:-10px;background:var(--teal);color:var(--white);border-radius:20px;padding:11px 20px;white-space:nowrap;font-weight:600}

/* hero */
.hero{height:544px;position:relative;background:linear-gradient(90deg,#262626 0%,#3d3d3d 40%,#8a8a8a 70%,#cfcfcf 100%)}
.hero-copy{position:absolute;left:141px;top:137px}
.hero h1{font:700 36px/1.18 'Montserrat',sans-serif;letter-spacing:1px;text-transform:uppercase}
.hero h1 .accent{color:var(--teal);display:block}
.hero h1 .plain{color:var(--white);display:block}
.hero p{color:var(--white);font:500 18px/1.55 'Montserrat',sans-serif;margin-top:14px;width:440px}
.hero .cta{margin-top:22px;display:inline-flex;align-items:center;gap:12px;background:var(--blue);color:var(--white);font:600 16px 'Montserrat',sans-serif;border-radius:26px;padding:8px 8px 8px 24px}
.hero .cta span{width:36px;height:36px;border-radius:50%;background:var(--white);display:flex;align-items:center;justify-content:center}

/* how it works */
.how{height:543px;padding-top:74px}
.steps{display:flex;justify-content:space-between;margin-top:44px}
.step{width:290px;text-align:center}
.step .icon{width:102px;height:102px;border-radius:50%;background:#5c9cd6;margin:0 auto;display:flex;align-items:center;justify-content:center}
.step h3{font:600 22px 'Roboto Slab',serif;margin-top:22px}
.step p{font:400 12.5px/1.8 'Roboto',sans-serif;color:var(--muted);margin:8px auto 0;width:230px}
.how .center{text-align:center;margin-top:38px}

/* about */
.about{height:533px;background:var(--soft);padding-top:85px}
.about .wrap{display:flex}
.about-media{width:430px;height:362px;position:relative}
.about-media .room{position:absolute;left:102px;top:0;width:330px;height:282px;border-radius:8px;background:linear-gradient(135deg,#c7a785,#efe8de 45%,#d8cfc4)}
.about-media .worker{position:absolute;left:0;top:192px;width:160px;height:170px;border-radius:8px;background:linear-gradient(160deg,#d8dde2,#5f6b78);border:3px solid var(--white)}
.about-copy{margin-left:50px;width:438px;padding-top:2px}
.about-copy h2{font:600 34px 'Roboto Slab',serif;color:var(--blue)}
.about-copy h4{font:600 14.5px 'Roboto Slab',serif;margin-top:22px}
.about-copy p{font:400 11.7px/1.95 'Roboto',sans-serif;color:var(--muted);margin-top:14px}
.about-copy .btn{margin-top:30px}

/* services */
.services{height:817px;padding-top:84px}
.grid{display:grid;grid-template-columns:444px 444px;gap:28px 30px;margin-top:44px}
.card{height:230px;background:var(--white);box-shadow:0 2px 12px rgba(0,0,0,.13);border-radius:6px;padding:26px 22px}
.card .svc-icon{width:62px;height:58px;background:linear-gradient(135deg,#cfe2f3,#8fbde6);border-radius:4px}
.card h3{font:500 21px 'Montserrat',sans-serif;margin-top:16px}
.card p{font:400 12.5px/1.8 'Roboto',sans-serif;color:var(--muted);margin-top:14px;width:390px}
.services .center{text-align:center;margin-top:36px}

/* reviews */
.reviews{height:512px;background:var(--soft);padding-top:86px;position:relative}
.rev-row{display:flex;justify-content:space-between;margin-top:44px;position:relative}
.review{width:290px;height:248px;background:var(--white);box-shadow:0 2px 12px rgba(0,0,0,.1);border-radius:6px;padding:50px 20px 0;position:relative}
.review .quote{position:absolute;right:18px;top:-22px;font:800 90px/1 'Montserrat',sans-serif;color:var(--blue);height:50px;overflow:hidden}
.review p{font:400 12.5px/1.8 'Roboto',sans-serif;color:var(--muted)}
.reviewer{display:flex;align-items:center;gap:14px;margin-top:30px}
.reviewer .avatar{width:54px;height:54px;border-radius:50%;background:linear-gradient(135deg,#d9d9d9,#9a9a9a)}
.reviewer b{font:700 13px 'Roboto',sans-serif;display:block}
.stars{color:#f1c232;font-size:13px;letter-spacing:1px}
.arrow{position:absolute;width:30px;height:30px;border-radius:50%;border:1.6px solid #333;display:flex;align-items:center;justify-content:center}

/* insurance */
.insurance{height:266px;padding-top:66px;position:relative}
.insurance h2{text-align:center;font:700 32px 'Montserrat',sans-serif;color:var(--teal);letter-spacing:.5px}
.insurance h2 span{color:var(--blue)}
.partners{display:flex;justify-content:space-between;margin-top:24px}
.partner{width:170px;height:92px;background:var(--white);box-shadow:0 2px 8px rgba(0,0,0,.12);border-bottom:3px solid var(--teal);display:flex;align-items:center;justify-content:center;gap:8px;font:700 17px 'Montserrat',sans-serif;color:var(--blue)}
.partner i{width:14px;height:14px;background:var(--blue);display:block;border-radius:50%}
.ins-arrow{position:absolute;top:157px;width:38px;height:38px;border-radius:50%;display:flex;align-items:center;justify-content:center}

/* cta */
.cta-band{height:485px;padding-top:46px}
.cta-band .wrap{display:flex;justify-content:space-between;align-items:center}
.cta-band h2{font:600 39px/1.27 'Roboto Condensed',sans-serif;color:var(--ink)}
.cta-band .btn{border-radius:2px;margin-top:14px;padding:10px 18px}
.cta-media{width:445px;height:354px;border-radius:8px;background:linear-gradient(135deg,#cfd8e3,#5e8fd6 55%,#2b5ea8)}

/* footer */
.site-footer{height:295px;background:var(--footer);color:var(--white);padding-top:50px}
.site-footer .wrap{display:flex}
.site-footer h5{font:700 15px 'Montserrat',sans-serif;letter-spacing:.5px;margin-bottom:14px}
.links li{list-style:none;font:400 12px 'Roboto',sans-serif;margin-bottom:15px}
.links li::before{content:"• "}
.col-links{width:205px}
.col-contact{width:284px}
.contact-row{display:flex;gap:12px;margin-bottom:16px;font:400 12px/1.6 'Roboto',sans-serif}
.contact-row b{font-weight:500;display:block}
.col-follow{width:196px}
.follow{display:flex;align-items:center;gap:12px;font:400 12px 'Roboto',sans-serif;margin-bottom:14px}
.follow span{width:28px;height:28px;border:1px solid #888;display:block}
.foot-logo{margin-top:36px;display:flex;align-items:center;gap:12px;font:700 30px 'Montserrat',sans-serif;color:var(--teal)}
.foot-logo i{width:40px;height:40px;background:var(--blue);display:block;border-radius:4px}
.copyright{height:43px;background:var(--teal);color:var(--ink);font:400 12px 'Montserrat',sans-serif;display:flex;align-items:center;justify-content:center}
</style>
</head>
<body>

<header class="site-header">
  <div class="topbar">
    <div class="item">
      <svg width="18" height="18" viewBox="0 0 24 24" fill="none" stroke="#fff" stroke-width="2"><path d="M5 3h4l2 5-3 2a11 11 0 0 0 6 6l2-3 5 2v4a2 2 0 0 1-2 2A17 17 0 0 1 3 5a2 2 0 0 1 2-2z"/></svg>
      <span>Call or Text: <b>(555) 014-2290</b></span>
    </div>
    <div class="item">
      <svg width="16" height="12" viewBox="0 0 16 12"><rect width="16" height="12" rx="1" fill="#fff"/><path d="M0 1l8 6 8-6" stroke="#2f80c6" stroke-width="1.5" fill="none"/></svg>
      <span>hello@clearspotclean.com</span>
    </div>
    <div class="socials"><span></span><span></span><span></span></div>
  </div>
  <div class="logo"><i></i>ClearSpot Cleaning</div>
  <nav class="nav">
    <span class="active">Home</span><span>About</span><span>Our Services ⌄</span><span>Reviews</span><span>Blog</span><span>Contact</span>
    <span class="quote">Request A Quote</span>
  </nav>
</header>

<section class="hero" role="img" aria-label="Photo of a cleaner steam-cleaning a floor">
  <div class="hero-copy">
    <h1><span class="accent">Hassle Free</span><span class="accent">Cleaning Solution</span><span class="plain">For Your Property</span></h1>
    <p>Quality driven and reliable to take care of all your cleaning neess!!!</p>
    <div class="cta">Request A Quote <span><svg width="14" height="14" viewBox="0 0 14 14"><path d="M5 2l5 5-5 5" stroke="#2f80c6" stroke-width="2" fill="none"/></svg></span></div>
  </div>
</section>

<section class="how">
  <div class="wrap">
    <h2 class="section-title">How It Works</h2>
    <div class="steps">
      <div class="step">
        <div class="icon"><svg width="46" height="46" viewBox="0 0 46 46" fill="none" stroke="#fff" stroke-width="2"><rect x="10" y="4" width="24" height="38" rx="3"/><path d="M16 22l5 5 9-10"/></svg></div>
        <h3>Book a Clean Online</h3>
        <p>Lorem Ipsum has been the industry's standard dummy text ever since the 1500s, when an unknown</p>
      </div>
      <div class="step">
        <div class="icon"><svg width="46" height="46" viewBox="0 0 46 46" fill="none" stroke="#fff" stroke-width="2"><rect x="8" y="18" width="14" height="22" rx="2"/><path d="M12 18v-6h6v6M32 6v26M27 32h10l-2 8h-6z"/></svg></div>
        <h3>We do The Clean Work</h3>
        <p>Lorem Ipsum has been the industry's standard dummy text ever since the 1500s, when an unknown</p>
      </div>
      <div class="step">
        <div class="icon"><svg width="46" height="46" viewBox="0 0 46 46" fill="none" stroke="#fff" stroke-width="2"><circle cx="32" cy="12" r="5"/><path d="M6 30l14 4 18-6M10 32l-2 8M36 30l2 10"/></svg></div>
        <h3>You Sit Back And Relax</h3>
        <p>Lorem Ipsum has been the industry's standard dummy text ever since the 1500s, when an unknown</p>
      </div>
    </div>
    <div class="center"><span class="btn">Book A Cleaning</span></div>
  </div>
</section>

<section class="about">
  <div class="wrap">
    <div class="about-media">
      <div class="room" role="img" aria-label="Photo of a bright, tidy living room"></div>
      <div class="worker" role="img" aria-label="Photo of a cleaner vacuuming an office corridor"></div>
    </div>
    <div class="about-copy">
      <h2>About Us</h2>
      <h4>Lorem Ipsum is simply dummy and typesetting industry.</h4>
      <p>Lorem Ipsum is simply dummy text of the printing and typesetting industry. Lorem Ipsum has been the industry's standard dummy text ever since the to same 1500s, when an unknown printer took a galley of type and scrambled it to type specimen book. It has survived not only five centuries, but also the leap into electronic typesetting, remaining essentially unchanged.</p>
      <p>Lorem Ipsum is simply dummy text of the printing and typesetting industry. to Lorem Ipsum has been the industry's standard dummy text ever since the 1500s, when an unknown printer took a galley make a type of specimen book.</p>
      <span class="btn">Read More</span>
    </div>
  </div>
</section>

<section class="services">
  <div class="wrap">
    <h2 class="section-title">Services We Offer</h2>
    <div class="grid">
      <div class="card"><div class="svc-icon" role="img" aria-label="House icon"></div><h3>Residential Cleaning</h3><p>Lorem Ipsum has been the industry's standard dummy text ever since the 1500s, when an printer took read specimen book.</p></div>
      <div class="card"><div class="svc-icon" role="img" aria-label="Office building icon"></div><h3>Commercial Cleaning</h3><p>Lorem Ipsum has been the industry's standard dummy text ever since the 1500s, when an printer took read specimen book.</p></div>
      <div class="card"><div class="svc-icon" role="img" aria-label="Sanitizing hand icon"></div><h3>Antiviral Disinfection</h3><p>Lorem Ipsum has been the industry's standard dummy text ever since the 1500s, when an printer took read specimen book.</p></div>
      <div class="card"><div class="svc-icon" role="img" aria-label="Construction cleanup icon"></div><h3>Construction Cleaning</h3><p>Lorem Ipsum has been the industry's standard dummy text ever since the 1500s, when an printer took read specimen book.</p></div>
    </div>
    <div class="center"><span class="btn">Book A Cleaning</span></div>
  </div>
</section>

<section class="reviews">
  <div class="wrap">
    <h2 class="section-title">Customer Reviews</h2>
    <div class="rev-row">
      <div class="review"><div class="quote">”</div><p>Lorem Ipsum has been the industry's standard dummy text ever since the 1500s, when an printer took read the specimen book.</p><div class="reviewer"><div class="avatar" role="img" aria-label="Customer portrait"></div><div><b>Dane Porter</b><span class="stars">★★★★★</span></div></div></div>
      <div class="review"><div class="quote">”</div><p>Lorem Ipsum has been the industry's standard dummy text ever since the 1500s, when an printer took read the specimen book.</p><div class="reviewer"><div class="avatar" role="img" aria-label="Customer portrait"></div><div><b>Leo Marsh</b><span class="stars">★★★★★</span></div></div></div>
      <div class="review"><div class="quote">”</div><p>Lorem Ipsum has been the industry's standard dummy text ever since the 1500s, when an printer took read the specimen book.</p><div class="reviewer"><div class="avatar" role="img" aria-label="Customer portrait"></div><div><b>Nina Reyes</b><span class="stars">★★★★★</span></div></div></div>
      <div class="arrow" style="left:-45px;top:110px"><svg width="14" height="12" viewBox="0 0 14 12"><path d="M13 6H2M6 1L1 6l5 5" stroke="#333" stroke-width="1.5" fill="none"/></svg></div>
      <div class="arrow" style="right:-45px;top:110px"><svg width="14" height="12" viewBox="0 0 14 12"><path d="M1 6h11M8 1l5 5-5 5" stroke="#333" stroke-width="1.5" fill="none"/></svg></div>
    </div>
  </div>
</section>

<section class="insurance">
  <div class="wrap">
    <h2>INSURANCE COMPANIES <span>WE SUPPORT</span></h2>
    <div class="partners">
      <div class="partner"><i></i>Harbor Health</div>
      <div class="partner"><i></i>Elder Mutual</div>
      <div class="partner"><i></i>Crestline</div>
      <div class="partner"><i></i>Unity Shield</div>
      <div class="partner"><i></i>Lifeway Trust</div>
    </div>
  </div>
  <div class="ins-arrow" style="left:83px;border:2px solid var(--blue)"><svg width="16" height="14" viewBox="0 0 16 14"><path d="M15 7H2M7 1L1 7l6 6" stroke="#2f80c6" stroke-width="2" fill="none"/></svg></div>
  <div class="ins-arrow" style="left:1078px;background:var(--blue)"><svg width="16" height="14" viewBox="0 0 16 14"><path d="M1 7h13M9 1l6 6-6 6" stroke="#fff" stroke-width="2" fill="none"/></svg></div>
</section>

<section class="cta-band">
  <div class="wrap">
    <div>
      <h2>Expert Cleaning And<br>Maintenance Services<br>For Your Home or Business</h2>
      <span class="btn">Contact Us</span>
    </div>
    <div class="cta-media" role="img" aria-label="Photo of a bucket of cleaning supplies"></div>
  </div>
</section>

<footer class="site-footer">
  <div class="wrap">
    <div class="col-links">
      <h5>QUICK LINKS</h5>
      <ul class="links"><li>Home</li><li>About Us</li><li>Services</li><li>Insurance</li><li>Contact Us</li></ul>
    </div>
    <div class="col-contact">
      <h5>CONTACT DETAILS</h5>
      <div class="contact-row"><svg width="12" height="16" viewBox="0 0 12 16"><path d="M6 0a6 6 0 0 1 6 6c0 4-6 10-6 10S0 10 0 6a6 6 0 0 1 6-6z" fill="#fff"/><circle cx="6" cy="6" r="2" fill="#0c0c0c"/></svg><div><b>Address</b>123 Ut Wisi Enim Ad Minim<br>Veniam Quis, City Name.</div></div>
      <div class="contact-row"><svg width="13" height="13" viewBox="0 0 24 24"><path d="M5 2h4l2 5-3 2a11 11 0 0 0 6 6l2-3 5 2v4a2 2 0 0 1-2 2A18 18 0 0 1 3 4a2 2 0 0 1 2-2z" fill="#fff"/></svg><div><b>Phone</b>(555) 014-2290</div></div>
      <div class="contact-row"><svg width="13" height="10" viewBox="0 0 16 12"><rect width="16" height="12" rx="1" fill="#fff"/><path d="M0 1l8 6 8-6" stroke="#0c0c0c" stroke-width="1.5" fill="none"/></svg><div><b>Email</b>hello@clearspotclean.com</div></div>
    </div>
    <div class="col-follow">
      <h5>FOLLOW US</h5>
      <div class="follow"><span></span>Friendbook</div>
      <div class="follow"><span></span>Linkwork</div>
      <div class="follow"><span></span>Snapgram</div>
      <div class="follow"><span></span>Chirper</div>
    </div>
    <div class="foot-logo"><i></i>ClearSpot<br>Cleaning</div>
  </div>
</footer>
<div class="copyright">© 2024 ClearSpot Cleaning. All Rights Reserved.</div>

</body>
</html>
```